Zielgruppe
Zielgruppe sind Großhändler in der Elektrotechnik, Fachfirmen für Notbeleuchtung. Produkte: Notbeleuchtungssysteme, Not- und Sicherheitsleuchten, Akkumulatoren/Batterien (industrielle)
Aufgabenstellung
Optimale Darstellung des Logos und der Werte des Unternehmens. Einhaltung der Farben des Logos. Eher eine helle Businesskarte, nicht zu Dunkel.
Wir bitten, dass uns der Gewinner gleich für die ersten 6 Mitarbeiter, welche Visitenkarten in unserem Unternehmen benötigen, zu erstellen.
Die bestehende Visitenkarte kam leider nicht gut an. Falsche Farben und kein komplett abgestimmtes Design.
Die neue Visitenkarte soll gut zur Website passen und die Firma optimal repräsentieren.
!Bitte nicht die Farbe der bestehenden Visitenkarte benutzen sondern nur Farbtöne des Logos. Bitte nicht zwingend am bestehenden Design der Visitenkarte orientieren, wir möchten frische Ideen!

```html
<!DOCTYPE html>
<html lang="de">
<head>
<meta charset="utf-8">
<title>Korvel Systems – Visitenkarte</title>
<link href="https://fonts.googleapis.com/css2?family=Open+Sans:wght@400;600;700;800&display=swap" rel="stylesheet">
<style>
  :root {
    --magenta: #b0126e;
    --grey: #6d6e71;
    --grey-dark: #58595b;
    --grey-light: #a7a9ac;
    --card: #ffffff;
    --backdrop: #eceef0;
  }
  * { box-sizing: border-box; margin: 0; padding: 0; }
  html, body { width: 1200px; height: 720px; overflow: hidden; }
  body {
    background: var(--backdrop);
    font-family: "Open Sans", Arial, sans-serif;
    color: var(--grey);
    position: relative;
  }
  .card {
    position: absolute;
    top: 185px;
    width: 540px;
    height: 350px;
    background: var(--card);
    overflow: hidden;
    box-shadow: 0 2px 10px rgba(0,0,0,0.08);
  }
  .card--front { left: 40px; }
  .card--back { left: 620px; }

  /* Front */
  .halftone {
    position: absolute;
    left: 0; top: 0;
    width: 540px; height: 350px;
  }
  .person { position: absolute; left: 30px; top: 58px; text-align: right; }
  .person__name { font-size: 26px; font-weight: 700; color: var(--grey-dark); line-height: 1; }
  .person__role { font-size: 11px; line-height: 1.35; margin-top: 8px; }
  .company { position: absolute; left: 290px; top: 30px; }
  .company__name { font-size: 16px; font-weight: 700; color: var(--magenta); }
  .company__address { font-size: 15px; line-height: 1.3; margin-top: 2px; }
  .divider { position: absolute; left: 365px; top: 112px; width: 175px; height: 1px; background: var(--grey-light); }
  .contacts { position: absolute; left: 30px; top: 152px; list-style: none; }
  .contacts li { display: flex; align-items: center; gap: 10px; font-size: 16px; line-height: 1; margin-bottom: 9px; }
  .contacts svg { width: 17px; height: 17px; flex: none; }

  .url-band {
    position: absolute;
    left: 0; right: 0;
    background: var(--magenta);
    color: #fff;
    font-weight: 800;
    text-align: right;
    padding-right: 30px;
  }
  .card--front .url-band { top: 256px; height: 34px; line-height: 34px; font-size: 20px; }

  /* Back */
  .brand { position: absolute; left: 0; right: 0; top: 66px; display: flex; justify-content: center; align-items: center; gap: 12px; }
  .brand__dot { width: 18px; height: 18px; border-radius: 50%; background: var(--magenta); }
  .brand__name { font-size: 30px; font-weight: 700; color: var(--grey-dark); line-height: 1; }
  .card--back .url-band { top: 148px; height: 38px; line-height: 38px; font-size: 21px; }
  .values { position: absolute; left: 20px; right: 20px; top: 212px; display: flex; justify-content: space-around; list-style: none; }
  .values li { width: 110px; text-align: center; }
  .values svg { width: 54px; height: 54px; }
  .values span { display: block; margin-top: 8px; font-size: 11px; font-weight: 700; line-height: 1.3; color: var(--grey); text-transform: uppercase; }
</style>
</head>
<body>

<section class="card card--front">
  <svg class="halftone" viewBox="0 0 540 350" role="img" aria-label="Grauer Halbton-Punkteverlauf als Hintergrundmuster">
    <defs>
      <linearGradient id="dotsFadeTop" x1="0" y1="0" x2="1" y2="0">
        <stop offset="0" stop-color="#a7a9ac" stop-opacity="0"/>
        <stop offset="0.6" stop-color="#a7a9ac" stop-opacity="0.4"/>
        <stop offset="1" stop-color="#a7a9ac" stop-opacity="0.65"/>
      </linearGradient>
      <linearGradient id="dotsFadeBottom" x1="0" y1="0" x2="1" y2="0">
        <stop offset="0" stop-color="#a7a9ac" stop-opacity="0.5"/>
        <stop offset="1" stop-color="#a7a9ac" stop-opacity="0"/>
      </linearGradient>
    </defs>
    <path d="M340 256 C410 210 470 175 540 150 L540 256 Z" fill="url(#dotsFadeTop)"/>
    <path d="M0 290 L320 290 C220 310 100 330 0 345 Z" fill="url(#dotsFadeBottom)"/>
  </svg>

  <div class="person">
    <p class="person__name">Lutz Bramer</p>
    <p class="person__role">Geschäftsführer<br>Managing Director</p>
  </div>

  <div class="company">
    <p class="company__name">Korvel Systems GmbH</p>
    <p class="company__address">Lindenweg 4<br>D-83410 Seebach</p>
  </div>
  <div class="divider"></div>

  <ul class="contacts">
    <li>
      <svg viewBox="0 0 20 20"><circle cx="10" cy="10" r="10" fill="var(--magenta)"/><path d="M7 5.5l1.6 2.3-1 1.1c.6 1.3 1.5 2.2 2.6 2.7l1.1-1 2.2 1.5-.8 1.7c-3.4-.3-6.3-3.2-6.6-6.6z" fill="#fff"/></svg>
      08661 40217 33
    </li>
    <li>
      <svg viewBox="0 0 20 20"><circle cx="10" cy="10" r="10" fill="var(--magenta)"/><path d="M7 5.5l1.6 2.3-1 1.1c.6 1.3 1.5 2.2 2.6 2.7l1.1-1 2.2 1.5-.8 1.7c-3.4-.3-6.3-3.2-6.6-6.6z" fill="#fff"/></svg>
      0171-2208459
    </li>
    <li>
      <svg viewBox="0 0 20 20"><circle cx="10" cy="10" r="10" fill="var(--magenta)"/><rect x="5" y="6.5" width="10" height="7" fill="none" stroke="#fff" stroke-width="1.3"/><path d="M5 6.8l5 4 5-4" fill="none" stroke="#fff" stroke-width="1.3"/></svg>
      lutz.bramer@korvel-systems.com
    </li>
  </ul>

  <div class="url-band">www.korvel-systems.com</div>
</section>

<section class="card card--back">
  <div class="brand">
    <span class="brand__dot"></span>
    <span class="brand__name">Korvel Systems</span>
  </div>

  <div class="url-band">www.korvel-systems.com</div>

  <ul class="values">
    <li>
      <svg viewBox="0 0 54 54" fill="none" stroke="var(--magenta)" stroke-width="2.5">
        <circle cx="27" cy="27" r="10"/>
        <circle cx="27" cy="27" r="4"/>
        <path d="M27 9v6M27 39v6M9 27h6M39 27h6M14.3 14.3l4.2 4.2M35.5 35.5l4.2 4.2M14.3 39.7l4.2-4.2M35.5 18.5l4.2-4.2"/>
      </svg>
      <span>Technology</span>
    </li>
    <li>
      <svg viewBox="0 0 54 54" fill="none" stroke="var(--magenta)" stroke-width="2.5">
        <circle cx="27" cy="27" r="20"/>
        <circle cx="21" cy="27" r="7"/>
        <circle cx="33" cy="27" r="7"/>
      </svg>
      <span>Partnership</span>
    </li>
    <li>
      <svg viewBox="0 0 54 54" fill="none" stroke="var(--magenta)" stroke-width="2.5">
        <rect x="15" y="10" width="24" height="38" rx="2"/>
        <rect x="22" y="6" width="10" height="4"/>
        <path d="M20 20h14M20 28h14M20 36h14"/>
      </svg>
      <span>Battery-<br>Power</span>
    </li>
    <li>
      <svg viewBox="0 0 54 54" fill="none" stroke="var(--magenta)" stroke-width="2.5">
        <circle cx="27" cy="27" r="20"/>
        <circle cx="27" cy="27" r="13"/>
        <path d="M21 27l4.5 4.5L34 23"/>
      </svg>
      <span>Premium<br>Quality</span>
    </li>
  </ul>
</section>

</body>
</html>
```